iPhone iOS 7 App For Managing Tasks/Photos for Internal Company Use

We need an app design that displays company objectives and task, and provides the interface for employees to complete a task by uploading a photo and adding comments.

Please see attached mock up sketches as a rough guideline

Final delivery of files must contain PSD, and all layers/objects sliced both is PSD and PNG files

Target Market(s)

This is a tool for internal employee use

Industry/Entity Type

It Company

Requirements
Must have
• Must include logo, and match the colour scheme
Use iPhone iOS 7 Style

```html
<!DOCTYPE html>
<html lang="en">
<head>
<meta charset="utf-8">
<title>Objectives Progress</title>
<link rel="stylesheet" href="https://fonts.googleapis.com/css2?family=Carlito:wght@400;700&family=Roboto:wght@400;500&display=swap">
<style>
  :root {
    --bg: #a8bbc6;
    --header-bg: #ffffff;
    --ink: #456a71;
    --ink-dark: #3f5f66;
    --status-ink: #000000;
    --ring-outer: #ffffff;
    --ring-track: #e3eaeb;
    --ring-fill-start: #9ab8b9;
    --ring-fill-end: #5f8187;
    --nav-band: #5e7c82;
    --nav-face: #eef0f0;
    --nav-icon: #7d8a8c;
  }
  * { margin: 0; padding: 0; box-sizing: border-box; }
  html, body { width: 675px; height: 1200px; overflow: hidden; }
  body { background: var(--bg); font-family: "Carlito", Calibri, sans-serif; position: relative; }
  .status-bar {
    position: absolute; top: 0; left: 0; width: 675px; height: 51px;
    font-family: "Roboto", Helvetica, sans-serif; font-size: 23px; color: var(--status-ink);
  }
  .status-bar .carrier { position: absolute; left: 14px; top: 10px; display: flex; align-items: center; gap: 6px; }
  .status-bar .time { position: absolute; left: 0; right: 0; top: 10px; text-align: center; font-weight: 500; }
  .status-bar .battery-group { position: absolute; right: 12px; top: 10px; display: flex; align-items: center; gap: 8px; }
  .app-header {
    position: absolute; top: 51px; left: 0; width: 675px; height: 84px;
    background: var(--header-bg); box-shadow: 0 2px 4px rgba(0,0,0,0.25);
    display: flex; align-items: center; justify-content: center; gap: 14px;
  }
  .app-header .brand, .app-header .company-name {
    font-weight: 700; font-size: 36px; color: var(--ink); letter-spacing: 0.3px;
  }
  .progress-dial { position: absolute; left: 0; top: 0; }
  .dial-label {
    position: absolute; left: 366px; top: 488px; transform: translateX(-50%);
    text-align: center; white-space: nowrap;
    font-weight: 700; color: var(--ink); line-height: 1.05;
  }
  .dial-label .percent { font-size: 48px; display: block; }
  .dial-label .word { font-size: 50px; display: block; }
  .objectives-summary {
    position: absolute; top: 897px; left: 0; width: 675px; text-align: center;
    font-weight: 700; font-size: 37px; color: var(--ink-dark); letter-spacing: 0.3px;
  }
  .tab-bar { position: absolute; left: 0; top: 1040px; width: 675px; height: 160px; }
  .tab-labels { position: absolute; top: 1140px; left: 0; width: 675px; }
  .tab-labels span {
    position: absolute; transform: translateX(-50%); white-space: nowrap;
    font-weight: 700; font-size: 31px; color: var(--ink-dark);
  }
</style>
</head>
<body>
  <div class="status-bar">
    <div class="carrier">
      <svg width="78" height="16" viewBox="0 0 78 16" aria-hidden="true">
        <circle cx="7" cy="8" r="6.5" fill="#000"/>
        <circle cx="22" cy="8" r="6.5" fill="#000"/>
        <circle cx="37" cy="8" r="6.5" fill="#000"/>
        <circle cx="52" cy="8" r="6" fill="none" stroke="#000" stroke-width="1.2"/>
        <circle cx="67" cy="8" r="6" fill="none" stroke="#000" stroke-width="1.2"/>
      </svg>
      <span>CELVO</span>
      <svg width="26" height="20" viewBox="0 0 26 20" aria-hidden="true">
        <path d="M13 19 L8 13 A7 7 0 0 1 18 13 Z" fill="#000"/>
        <path d="M3 8 A14 14 0 0 1 23 8" fill="none" stroke="#000" stroke-width="3"/>
        <path d="M6 11.5 A10 10 0 0 1 20 11.5" fill="none" stroke="#000" stroke-width="3"/>
      </svg>
    </div>
    <div class="time">4:21 PM</div>
    <div class="battery-group">
      <svg width="14" height="24" viewBox="0 0 14 24" aria-hidden="true">
        <path d="M2 6 L12 17 L7 22 L7 2 L12 7 L2 18" fill="none" stroke="#000" stroke-width="1.8"/>
      </svg>
      <span>100%</span>
      <svg width="50" height="22" viewBox="0 0 50 22" aria-hidden="true">
        <rect x="1" y="1" width="43" height="20" rx="3" fill="none" stroke="#000" stroke-width="1.5"/>
        <rect x="3.5" y="3.5" width="38" height="15" rx="1.5" fill="#000"/>
        <rect x="45" y="7" width="3.5" height="8" rx="1" fill="#000"/>
      </svg>
    </div>
  </div>

  <header class="app-header">
    <span class="brand">QENTORA</span>
    <span class="company-name">COMPANY NAME</span>
  </header>

  <svg class="progress-dial" width="675" height="1040" viewBox="0 0 675 1040" aria-hidden="true">
    <defs>
      <linearGradient id="ring-fill" gradientUnits="userSpaceOnUse" x1="366" y1="320" x2="300" y2="740">
        <stop offset="0" stop-color="var(--ring-fill-start)"/>
        <stop offset="1" stop-color="var(--ring-fill-end)"/>
      </linearGradient>
      <radialGradient id="face" cx="0.5" cy="0.35" r="0.7">
        <stop offset="0" stop-color="#ffffff"/>
        <stop offset="1" stop-color="#f1f2f2"/>
      </radialGradient>
      <filter id="soft-shadow" x="-20%" y="-20%" width="140%" height="140%">
        <feDropShadow dx="0" dy="2" stdDeviation="3" flood-color="#000" flood-opacity="0.22"/>
      </filter>
    </defs>
    <circle cx="366" cy="540" r="237" fill="var(--ring-outer)" filter="url(#soft-shadow)"/>
    <circle cx="366" cy="540" r="198" fill="none" stroke="var(--ring-track)" stroke-width="38"/>
    <circle cx="366" cy="540" r="198" fill="none" stroke="url(#ring-fill)" stroke-width="38"
            stroke-dasharray="808.7 1244.1" transform="rotate(-90 366 540)"/>
    <circle cx="366" cy="540" r="181" fill="url(#face)" filter="url(#soft-shadow)"/>
  </svg>

  <div class="dial-label">
    <span class="percent">65%</span>
    <span class="word">COMPLETE</span>
  </div>

  <div class="objectives-summary">9/10 OBJECTIVES COMPLETE</div>

  <svg class="tab-bar" width="675" height="160" viewBox="0 0 675 160" aria-hidden="true">
    <path d="M102 38 C150 38 150 58 184 58 C218 58 218 38 264 38 C312 38 312 58 344 58 C376 58 376 38 422 38 C468 38 468 58 502 58 C536 58 536 38 583 38
             L583 64 C536 64 536 70 502 70 C468 70 468 64 422 64 C376 64 376 70 344 70 C312 70 312 64 264 64 C218 64 218 70 184 70 C150 70 150 64 102 64 Z"
          fill="var(--nav-band)"/>
    <g class="tab home">
      <circle cx="102" cy="52" r="41" fill="var(--nav-band)"/>
      <circle cx="102" cy="52" r="30" fill="var(--nav-face)"/>
      <path d="M84 54 L102 37 L120 54 M89 50 V67 H115 V50" fill="none" stroke="var(--nav-icon)" stroke-width="4" stroke-linejoin="round"/>
      <rect x="98" y="56" width="8" height="11" fill="var(--nav-icon)"/>
    </g>
    <g class="tab objectives">
      <circle cx="264" cy="52" r="41" fill="var(--nav-band)"/>
      <circle cx="264" cy="52" r="30" fill="var(--nav-face)"/>
      <circle cx="262" cy="55" r="15" fill="none" stroke="var(--nav-icon)" stroke-width="4"/>
      <circle cx="262" cy="55" r="7" fill="none" stroke="var(--nav-icon)" stroke-width="3"/>
      <path d="M262 55 L280 37 M275 36 L281 36 L281 42" fill="none" stroke="var(--nav-icon)" stroke-width="3" stroke-linecap="round"/>
    </g>
    <g class="tab news">
      <circle cx="422" cy="52" r="41" fill="var(--nav-band)"/>
      <circle cx="422" cy="52" r="30" fill="var(--nav-face)"/>
      <path d="M408 60 L428 38 L436 50 Z" fill="var(--nav-icon)"/>
      <path d="M410 58 L416 68" stroke="var(--nav-icon)" stroke-width="4" stroke-linecap="round"/>
      <path d="M435 36 A8 8 0 0 1 441 44 M438 31 A14 14 0 0 1 446 42" fill="none" stroke="var(--nav-icon)" stroke-width="2.5" stroke-linecap="round"/>
    </g>
    <g class="tab logout">
      <circle cx="583" cy="52" r="41" fill="var(--nav-band)"/>
      <circle cx="583" cy="52" r="30" fill="var(--nav-face)"/>
      <path d="M570 36 H588 V44 M588 60 V68 H570 Z" fill="none" stroke="var(--nav-icon)" stroke-width="3.5" stroke-linejoin="round"/>
      <path d="M570 36 L580 41 V72 L570 68 Z" fill="var(--nav-icon)"/>
      <path d="M584 52 H600 M594 45 L601 52 L594 59" fill="none" stroke="var(--nav-icon)" stroke-width="4" stroke-linecap="round" stroke-linejoin="round"/>
    </g>
  </svg>

  <nav class="tab-labels">
    <span style="left:100px">Home</span>
    <span style="left:268px">Objectives</span>
    <span style="left:417px">News</span>
    <span style="left:581px">Log Out</span>
  </nav>
</body>
</html>
```